KRWM new business card design

We need a business card design for our established business which is Australia wide however based in Melbourne. We are a young team of Financial Planners who specialize in Insurance and Basic super advice for people like us.

We are people who help our clients get things done in a timely and cost effective manner whilst having a good time and a laugh along the way.

We would like this to have a consistent feel with our new e-brochure which i have attached from a color and font perspective.

Industry/Entity Type

Business

Requirements
Must have
• We do not need specific address details rather just the states we are in:

VIC/NSW/QLD/TAS
Nice to have
• Curved edge to mate the brochure

```html
<!DOCTYPE html>
<html lang="en">
<head>
<meta charset="utf-8">
<title>KRWM Business Card</title>
<link rel="stylesheet" href="https://fonts.googleapis.com/css2?family=Arimo:wght@400;700&display=swap">
<style>
  :root {
    --page-bg: #e9e8e4;
    --card-dark: #262a27;
    --card-dark-green: #2f3b2c;
    --band-green: #4f7f3f;
    --edge-green: #58b25a;
    --lime: #9cc74a;
    --text-light: #ffffff;
    --text-soft: #e4ebdc;
  }
  * { margin: 0; padding: 0; box-sizing: border-box; }
  html, body {
    width: 1200px;
    height: 900px;
    overflow: hidden;
    background: var(--page-bg);
    font-family: "Arimo", Arial, sans-serif;
  }
  .canvas { position: relative; width: 1200px; height: 900px; }

  .card {
    position: absolute;
    width: 600px;
    height: 343px;
    background: var(--card-dark);
    overflow: hidden;
    box-shadow: 0 10px 28px rgba(0,0,0,0.28);
  }
  .card-front { left: 80px; top: 90px; }
  .card-back { left: 520px; top: 470px; }

  .front-band { position: absolute; inset: 0; }

  .brand {
    position: absolute;
    display: flex;
    align-items: center;
    gap: 16px;
    color: var(--text-light);
    font-weight: 700;
  }
  .brand-square { background: var(--lime); flex: none; }
  .brand-name { line-height: 1.1; }
  .brand-name span { display: block; white-space: nowrap; }

  .card-front .brand { left: 60px; top: 115px; }
  .card-front .brand-square { width: 110px; height: 110px; }
  .card-front .brand-name span:first-child { font-size: 26px; }
  .card-front .brand-name span:last-child { font-size: 13px; letter-spacing: 0.5px; }

  .back-tone {
    position: absolute;
    inset: 0;
    background: radial-gradient(ellipse at 78% 35%, var(--card-dark-green) 0%, rgba(47,59,44,0.4) 45%, rgba(38,42,39,0) 75%);
  }
  .card-back .brand {
    left: 40px; top: 95px;
    flex-direction: column;
    align-items: flex-start;
    gap: 10px;
  }
  .card-back .brand-square { width: 78px; height: 78px; }
  .card-back .brand-name span:first-child { font-size: 21px; }
  .card-back .brand-name span:last-child { font-size: 10px; letter-spacing: 0.4px; }

  .tagline {
    position: absolute;
    left: 140px; top: 98px;
    color: var(--text-light);
    font-weight: 700;
    font-size: 21px;
    line-height: 1.2;
    letter-spacing: 0.4px;
    white-space: nowrap;
  }
  .locations {
    position: absolute;
    right: 30px; top: 96px;
    list-style: none;
    text-align: right;
    color: var(--text-soft);
    font-size: 13px;
    line-height: 1.35;
    letter-spacing: 0.5px;
    white-space: nowrap;
  }
  .contact {
    position: absolute;
    left: 40px; bottom: 30px;
    color: var(--text-soft);
    font-size: 14px;
    font-style: normal;
    line-height: 1.35;
    letter-spacing: 0.3px;
  }
</style>
</head>
<body>
<main class="canvas">

  <section class="card card-front" aria-label="Business card front">
    <svg class="front-band" width="600" height="343" viewBox="0 0 600 343" aria-hidden="true">
      <path d="M372 0 H600 V343 H520 Q440 343 420 290 L385 40 Q380 10 372 0 Z" fill="var(--band-green)"/>
      <path d="M372 0 Q380 10 385 40 L420 290 Q440 343 520 343" fill="none" stroke="var(--edge-green)" stroke-width="7"/>
    </svg>
    <div class="brand">
      <div class="brand-square"></div>
      <div class="brand-name">
        <span>kestrel ridge</span>
        <span>WEALTH MANAGEMENT</span>
      </div>
    </div>
  </section>

  <section class="card card-back" aria-label="Business card back">
    <div class="back-tone"></div>
    <div class="brand">
      <div class="brand-square"></div>
      <div class="brand-name">
        <span>kestrel ridge</span>
        <span>WEALTH MANAGEMENT</span>
      </div>
    </div>
    <p class="tagline">SECURE FUTURE,<br>ENHANCED LIFESTYLE</p>
    <ul class="locations">
      <li>TASMANIA</li>
      <li>VICTORIA</li>
      <li>GOLD COAST</li>
      <li>NEW SOUTH WALES</li>
    </ul>
    <address class="contact">
      1300 555 214<br>
      admin@krwm.com.au<br>
      www.kestrelridgewealth.com.au
    </address>
  </section>

</main>
</body>
</html>
```